Vantage 9 Builders, Inc Biz Cards

Vantage 9 Builders, Inc is a turnkey building solution provider in the Greater Philadelphia Area. We work collaboratively with clients to provide turnkey building services in both the residential and commercial markets.
We are targeting the higher end clients in the commercial market. We have been successful in getting a few commercial projects in , but still rely on our residential work for a large portion of our revenue. We are trying to move almost exclusively toward the commercial market.
Services include;
-Commercial New Construction and Interior Tenant Fit-Outs
-Residential New Construction and Renovations
-Project Management and Owner's Representative Services
Target Market(s)
Tenants in large commerical buildings, higher end home owners, someone with a known budget and dream but unsure how to make it a building reality
Industry/Entity Type
Residential
Contact Information for Business Card
Vantage 9 Builders, Inc.
415 Maple Hollow
Brookhaven Falls, NJ 08512
There are three people that we need to order business cards for.
Dale Hunt
Cell# 302-555-0193
Dale@Vantage-9-Builders.example
Rory Velluzzi
Cell# 610-555-0147
Rory@Vantage-9-Builders.example
Ned Fox
Cell# 267-555-0128
Ned@Vantage-9-Builders.example
HIC#PA574920
www.vantage-9-builders.example (under construction)
We like our written our logo Vantage 9 Builders, Inc with red, blue, and grey. We do not like the V9B with spinning arrows as, however like the incorporation of the spinning around arrows to represent "turnkey" building services.
Look and feel

```html
<!DOCTYPE html>
<html lang="en">
<head>
<meta charset="utf-8">
<title>Vantage 9 Builders, Inc. – Business Card</title>
<link rel="stylesheet" href="https://fonts.googleapis.com/css2?family=Roboto:wght@400&family=PT+Sans:wght@400;700&family=Arimo:wght@400&display=swap">
<style>
  :root {
    --card-light: #ffffff;
    --card-mid: #eeeeee;
    --card-edge: #c9c9c9;
    --brand-blue: #1a8fd6;
    --ink: #111111;
    --tagline-grey: #a9a9a9;
  }
  html, body {
    margin: 0;
    padding: 0;
    width: 1200px;
    height: 703px;
    overflow: hidden;
  }
  .card {
    position: relative;
    width: 1200px;
    height: 703px;
    background: radial-gradient(ellipse 70% 75% at 48% 50%, var(--card-light) 0%, var(--card-mid) 45%, var(--card-edge) 100%);
    overflow: hidden;
  }
  .wordmark {
    position: absolute;
    left: 50px;
    top: 46px;
    margin: 0;
    font-family: "Roboto", Arial, sans-serif;
    font-weight: 400;
    font-size: 64px;
    line-height: 1;
    color: var(--brand-blue);
    white-space: nowrap;
  }
  .wordmark .suffix {
    font-size: 40px;
  }
  .contact {
    position: absolute;
    left: 0;
    top: 0;
    width: 1200px;
    height: 703px;
    text-align: center;
    font-family: "PT Sans", "Myriad Pro", sans-serif;
    color: var(--ink);
  }
  .contact p {
    position: absolute;
    left: 0;
    width: 100%;
    margin: 0;
    line-height: 1;
    white-space: nowrap;
  }
  .person-name { top: 262px; font-size: 56px; }
  .website     { top: 368px; font-size: 50px; }
  .address     { top: 422px; font-size: 36px; }
  .email       { top: 461px; font-size: 31px; }
  .phone       { top: 505px; font-size: 38px; font-weight: 700; }
  .tagline {
    position: absolute;
    left: 0;
    width: 1200px;
    top: 605px;
    margin: 0;
    text-align: center;
    font-family: "Arimo", Arial, sans-serif;
    font-size: 45px;
    line-height: 1;
    color: var(--tagline-grey);
    white-space: nowrap;
  }
</style>
</head>
<body>
  <main class="card">
    <h1 class="wordmark">Vantage 9 Builders <span class="suffix">Inc.</span></h1>
    <section class="contact">
      <p class="person-name">Dale Hunt</p>
      <p class="website">www.vantage-9-builders.example</p>
      <p class="address">415 Maple Hollow Brookhaven Falls, NJ 08512</p>
      <p class="email">Dale@Vantage-9-Builders.example</p>
      <p class="phone">302-555-0193</p>
    </section>
    <p class="tagline">Creative Planning. Dependable Construction.</p>
  </main>
</body>
</html>
```